Stationary for Hair Cosmetic company

We mainly sell hair thickening products www.morvello-wellform.de/morvello-hair/ Hair thickening products are a smart and easy solution for thinning hair for both men and women. We sell very information oriented in an honest undramatic manner.

We would like to see a decent color and style that is suitable for men and women. It shall be rather modern with a vintage spin as our own product (Morvello Bottle). Please use our logo (attatched).

Please bias your design to the bottle. To give you an idea: Chalk design like http://de.pixaverum.com/id/48213597 or one-color watercolor like http://de.pixaverum.com/id/63925180 is appreciated but not necessary.

Good but rejected designs will get compensation.

Target Market(s)

Wide range in demographics: age 20-55; 45% male, 55% women; issues with hair loss; self-conscious

Industry/Entity Type

Hair

Colors
3377b5
33a6d7
32b7a4
cbdf83
fbf289
fee18a
f9bb93
f05157

Requirements
Must have
• trustworthiness
Nice to have
• Chalk design like http://de.pixaverum.com/id/48213597 or one-color watercolor like http://de.pixaverum.com/id/63925180 is appreciated but not necessary

```html
<!DOCTYPE html>
<html lang="de">
<head>
<meta charset="utf-8">
<title>Morvello Hair – Business Cards</title>
<link rel="stylesheet" href="https://fonts.googleapis.com/css2?family=Michroma&family=Cormorant+Garamond:wght@500&display=swap">
<style>
  :root {
    --backdrop: #d3e4ea;
    --card-blue: #52b3e6;
    --ink-blue: #24527e;
    --card-white: #fbfbfa;
    --ink-dark: #2b2b2b;
    --ornament-blue: #3b6f9c;
    --ornament-dark: #555555;
  }
  html, body {
    margin: 0;
    width: 1200px;
    height: 1000px;
    overflow: hidden;
    background: var(--backdrop);
  }
  .canvas {
    position: relative;
    width: 1200px;
    height: 1000px;
  }
  .card {
    position: absolute;
    width: 500px;
    height: 300px;
    box-sizing: border-box;
  }
  .card--front {
    left: 80px;
    top: 200px;
    background: var(--card-blue);
  }
  .card--back {
    left: 620px;
    top: 480px;
    background: var(--card-white);
  }
  .brand-mark {
    position: absolute;
    border-radius: 50%;
  }
  .card--front .brand-mark {
    left: 200px;
    top: 62px;
    width: 96px;
    height: 96px;
    background: var(--ink-blue);
  }
  .card--back .brand-mark {
    left: 230px;
    top: 22px;
    width: 40px;
    height: 40px;
    background: var(--ink-dark);
  }
  .brand-name {
    position: absolute;
    left: 0;
    width: 100%;
    text-align: center;
    font-family: "Michroma", sans-serif;
    text-transform: uppercase;
    letter-spacing: 0.06em;
  }
  .card--front .brand-name {
    top: 172px;
    font-size: 14px;
    color: var(--ink-blue);
  }
  .card--back .brand-name {
    top: 68px;
    font-size: 7px;
    color: var(--ink-dark);
  }
  .accent-dot {
    position: absolute;
    width: 5px;
    height: 5px;
    border-radius: 50%;
    background: var(--card-white);
  }
  .ornament {
    position: absolute;
    width: 44px;
    height: 16px;
    border-radius: 8px;
    opacity: 0.55;
  }
  .card--front .ornament { background: var(--ornament-blue); }
  .card--back .ornament { background: var(--ornament-dark); opacity: 0.35; }
  .holder-name {
    position: absolute;
    top: 92px;
    width: 100%;
    text-align: center;
    font-family: "Michroma", sans-serif;
    font-size: 17px;
    letter-spacing: 0.14em;
    text-transform: uppercase;
    color: var(--ink-dark);
  }
  .holder-role {
    position: absolute;
    top: 118px;
    width: 100%;
    text-align: center;
    font-family: "Michroma", sans-serif;
    font-size: 10px;
    letter-spacing: 0.12em;
    color: var(--ink-dark);
  }
  .divider {
    position: absolute;
    left: 160px;
    top: 142px;
    width: 180px;
    height: 12px;
  }
  .contact {
    position: absolute;
    top: 168px;
    width: 100%;
    margin: 0;
    text-align: center;
    font-family: "Cormorant Garamond", serif;
    font-weight: 500;
    font-size: 13px;
    line-height: 17px;
    color: var(--ink-dark);
  }
</style>
</head>
<body>
<main class="canvas">

  <section class="card card--front" aria-label="Card front">
    <span class="brand-mark"></span>
    <span class="accent-dot" style="left:181px; top:108px;"></span>
    <span class="accent-dot" style="left:314px; top:108px;"></span>
    <span class="ornament" role="img" aria-label="Curled flourish ornament" style="left:360px; top:98px;"></span>
    <span class="ornament" role="img" aria-label="Curled flourish ornament" style="left:96px; top:160px;"></span>
    <div class="brand-name">Morvello Hair</div>
  </section>

  <section class="card card--back" aria-label="Card back">
    <span class="brand-mark"></span>
    <div class="brand-name">Morvello Hair</div>
    <span class="ornament" role="img" aria-label="Curled flourish ornament" style="left:400px; top:34px; width:34px; height:12px;"></span>
    <span class="ornament" role="img" aria-label="Curled flourish ornament" style="left:62px; top:150px; width:34px; height:12px;"></span>
    <div class="holder-name">Jonas Reiter</div>
    <div class="holder-role">Managing Officer</div>
    <svg class="divider" viewBox="0 0 180 12" aria-hidden="true">
      <line x1="6" y1="6" x2="174" y2="6" stroke="#2b2b2b" stroke-width="1.4"/>
      <path d="M0 6 L7 2 L7 10 Z" fill="#2b2b2b"/>
      <path d="M180 6 L173 2 L173 10 Z" fill="#2b2b2b"/>
    </svg>
    <p class="contact">
      Kessler und Brandt GbR<br>
      Lindenhofallee 14<br>
      65812 Talheim<br>
      Tel.: +49 (0) 6172 / 519 204 02<br>
      E-Mail: Kontakt@Morvello-Wellform.de<br>
      Web: www.morvello-wellform.de
    </p>
  </section>

</main>
</body>
</html>
```